New Business Card Design

we need a new business card as we have just moved location and need a fresh new look. we are a Land Surveying Company . the card needs to be 2 sided and needs to have what we do on the back as our previous card ( attached ).
i was thinking of maybe a ruler down the bottom of the card or something to make it stand out. size can be 90 x 55 or 90 x 45 .
maybe a shadow of the logo or something in the corner.
on the attached card where it says other offices , it should be Melbourne instead of bendigo

postal address should be there as PO box 812 , Thornbury Flats 3821
Updates

Reason: some designs didn't follow brief by having services provided on the back of the card, just giving a bit of time toi change and to review.

Industry/Entity Type

Business

Requirements
Must have
• All cards need to have services provided on the back please , as stated , a lot of designs have just had the logo on the back

```html
<!DOCTYPE html>
<html lang="en">
<head>
<meta charset="utf-8">
<title>Marlow Pike Land Surveyors – Business Card</title>
<link rel="stylesheet" href="https://fonts.googleapis.com/css2?family=Arimo:wght@400;700&display=swap">
<style>
  :root {
    --page-bg: #e4e5e7;
    --card-bg: #ffffff;
    --card-fade: #eef0f2;
    --band-deep: #1877c9;
    --band-mid: #3aa6e6;
    --band-light: #8fd8f6;
    --ink: #1e1f22;
    --ink-soft: #55585d;
    --ink-muted: #8a8d92;
    --name-grey: #a4a7ab;
    --brand-blue: #1c6fc0;
    --panel: #f1f2f4;
    --ghost: rgba(120, 130, 150, 0.08);
  }
  * { box-sizing: border-box; margin: 0; padding: 0; }
  html, body {
    width: 1200px; height: 1000px; overflow: hidden;
    background: var(--page-bg);
    font-family: "Arimo", Arial, sans-serif;
  }
  .sheet { position: relative; width: 1200px; height: 1000px; }

  .card {
    position: absolute; left: 250px; width: 700px; height: 428px;
    background: linear-gradient(135deg, var(--card-bg) 0%, var(--card-bg) 55%, var(--card-fade) 100%);
    box-shadow: 0 6px 18px rgba(0,0,0,0.12);
    overflow: hidden;
  }
  .card--front { top: 52px; }
  .card--back { top: 520px; }

  .top-band {
    position: absolute; left: 0; top: 0; width: 100%; height: 16px;
    background: linear-gradient(90deg, var(--band-deep) 0%, var(--band-mid) 55%, var(--band-light) 100%);
  }
  .top-band::after {
    content: ""; position: absolute; inset: 0;
    background: repeating-linear-gradient(90deg, rgba(255,255,255,0) 0 70px, rgba(255,255,255,0.14) 70px 110px);
  }

  .ghost-mark {
    position: absolute; width: 190px; height: 190px; border-radius: 50%;
    border: 14px solid var(--ghost); right: 36px; bottom: -20px;
  }

  /* front */
  .brand-panel {
    position: absolute; left: 24px; top: 46px; width: 676px; height: 110px;
    background: linear-gradient(90deg, var(--panel) 0%, var(--panel) 70%, rgba(241,242,244,0) 100%);
  }
  .brand {
    position: absolute; left: 40px; top: 56px; display: flex; align-items: center; gap: 22px;
  }
  .brand-dot { width: 88px; height: 88px; border-radius: 50%; background: var(--brand-blue); flex: none; }
  .brand-name {
    color: var(--ink); font-weight: 700; line-height: 1.05;
  }
  .brand-name .line-1 { display: block; font-size: 44px; letter-spacing: 1px; }
  .brand-name .line-2 { display: block; font-size: 24px; letter-spacing: 9px; margin-top: 4px; }

  .address {
    position: absolute; left: 40px; top: 182px;
    font-size: 14px; line-height: 19px; color: var(--ink-soft);
  }
  .contacts {
    position: absolute; left: 40px; top: 250px;
    border-collapse: collapse; font-size: 14px; line-height: 19px;
  }
  .contacts th { text-align: left; font-weight: 400; color: var(--ink-muted); width: 80px; }
  .contacts td.sep { color: var(--ink-muted); width: 16px; }
  .contacts td { color: var(--ink); }

  .person { position: absolute; left: 420px; top: 276px; }
  .person-name { font-size: 34px; color: var(--name-grey); letter-spacing: 1px; }
  .person-quals { font-size: 12px; line-height: 16px; color: var(--ink-muted); margin-top: 6px; }
  .person-role { font-size: 15px; line-height: 20px; color: var(--ink-soft); margin-top: 8px; }

  /* back */
  .services {
    position: absolute; left: 56px; top: 50px; padding-left: 14px;
    border-left: 1px solid var(--ink-muted);
    list-style: none; font-size: 15px; line-height: 21px; color: var(--ink-soft);
  }
  .services li::before { content: "- "; }
  .memberships {
    position: absolute; left: 70px; top: 232px;
    font-size: 14px; line-height: 20px; color: var(--ink-muted);
  }
  .offices { margin-top: 8px; }
  .offices strong { color: var(--ink-soft); font-weight: 400; margin-left: 6px; }
</style>
</head>
<body>
<main class="sheet">

  <section class="card card--front" aria-label="Business card front">
    <div class="top-band"></div>
    <div class="ghost-mark"></div>
    <div class="brand-panel"></div>
    <div class="brand">
      <span class="brand-dot"></span>
      <span class="brand-name">
        <span class="line-1">MARLOW PIKE</span>
        <span class="line-2">LAND SURVEYORS</span>
      </span>
    </div>

    <address class="address">
      Cnr Ashby Court and Linden Street,<br>
      Carrick East VIC 3822<br>
      PO box 812 , Thornbury Flats 3821
    </address>

    <table class="contacts">
      <tr><th>Telephone</th><td class="sep">:</td><td>03 5190 2261</td></tr>
      <tr><th>Facsimile</th><td class="sep">:</td><td>03 5190 2262</td></tr>
      <tr><th>Mobile</th><td class="sep">:</td><td>0412 608 377</td></tr>
      <tr><th>Email</th><td class="sep">:</td><td>daniel@marlowpike.com.au</td></tr>
      <tr><th>Website</th><td class="sep">:</td><td>www.marlowpike.com.au</td></tr>
    </table>

    <div class="person">
      <p class="person-name">Daniel Pike</p>
      <p class="person-quals">B.App.Sci.(Surv) MIS(Aust)<br>Grad.Dip.(Surv Prac)</p>
      <p class="person-role">Licensed Surveyor<br>Director</p>
    </div>
  </section>

  <section class="card card--back" aria-label="Business card back">
    <div class="top-band"></div>
    <div class="ghost-mark"></div>
    <ul class="services">
      <li>Subdivisions (Land and Building)</li>
      <li>Check Title Boundary Surveys</li>
      <li>Features and Level Surveys</li>
      <li>Neighbourhood and Site Description Plan For Development Permits</li>
      <li>Town Planning / Estate Designs</li>
      <li>Civil Engineering Surveys (Roads, Structural and Earthworks)</li>
    </ul>
    <div class="memberships">
      <p>Member of Regional Surveyors Guild</p>
      <p>Member of Urban Land Development Council</p>
      <p class="offices">Other Offices :<strong>Melbourne</strong></p>
    </div>
  </section>

</main>
</body>
</html>
```